Super elegant, crisp & clean Business card design required

We recently upgraded our branding - which is on our website - tavorelstudio.com

I would like a simple, yet elegant, clean business card design please.

The font of my logo is Cinzel - and because of the natural colour - it's best to have this on a black background.

I would like to have the back of the business card - with simply my logo.

PLEASE DO NOT SUBMIT A COMPLICATED / UNCLEAN DESIGN

Industry/Entity Type

Business

Contact Information for Business Card

Dalvik Ostrander Photography

Font styles to use
Other font styles liked:
• Cinzel

Requirements
Must have
• A backpage with nothing but my logo
• Simple design - stands out
Should not have
• Colour that dont align with my logo
• Over complicated '/ non symmetrical design

```html
<!DOCTYPE html>
<html lang="en">
<head>
<meta charset="utf-8">
<title>Dalvik Ostrander Photography — Business Card</title>
<link rel="stylesheet" href="https://fonts.googleapis.com/css2?family=Cinzel:wght@400;700&display=swap">
<style>
  :root {
    --stage: #2b2b2b;
    --card: #050505;
    --ink: #ffffff;
    --ink-soft: #d9d9d9;
  }
  * { margin: 0; padding: 0; box-sizing: border-box; }
  html, body { width: 1200px; height: 900px; overflow: hidden; }
  body {
    background: var(--stage);
    position: relative;
    font-family: 'Cinzel', serif;
    color: var(--ink);
  }
  .card {
    position: absolute;
    width: 560px;
    height: 320px;
    background: var(--card);
    border-radius: 22px;
    overflow: hidden;
    box-shadow: 0 18px 40px rgba(0,0,0,0.45);
  }
  .card--back { left: 90px; top: 90px; }
  .card--front { left: 550px; top: 490px; }

  .back-name {
    position: absolute;
    inset: 0;
    display: flex;
    align-items: center;
    justify-content: center;
    font-size: 34px;
    font-weight: 400;
    letter-spacing: 3px;
  }

  .brand {
    position: absolute;
    right: 40px;
    top: 44px;
    text-align: center;
  }
  .brand__name {
    font-size: 20px;
    font-weight: 400;
    letter-spacing: 1px;
  }
  .brand__tag {
    font-size: 10px;
    letter-spacing: 6px;
    color: var(--ink-soft);
    margin-top: 2px;
  }

  .contact {
    position: absolute;
    left: 40px;
    bottom: 38px;
  }
  .contact__marker {
    position: absolute;
    left: -40px;
    top: 10px;
    width: 28px;
    height: 16px;
    background: var(--ink);
  }
  .contact__name {
    font-size: 22px;
    font-weight: 700;
    letter-spacing: 0.5px;
  }
  .contact__role {
    font-size: 14px;
    color: var(--ink-soft);
    margin-bottom: 8px;
  }
  .contact__list { list-style: none; }
  .contact__item {
    display: flex;
    align-items: center;
    gap: 10px;
    font-size: 13px;
    line-height: 22px;
    color: var(--ink-soft);
  }
  .contact__item svg { width: 13px; height: 13px; flex: none; }

  .edge-band {
    position: absolute;
    left: 340px;
    right: 0;
    bottom: 0;
    height: 8px;
    background: var(--ink);
  }
</style>
</head>
<body>
  <section class="card card--back" aria-label="Card back">
    <div class="back-name">Dalvik Ostrander</div>
  </section>

  <section class="card card--front" aria-label="Card front">
    <div class="brand">
      <div class="brand__name">Dalvik Ostrander</div>
      <div class="brand__tag">PHOTOGRAPHY</div>
    </div>

    <div class="contact">
      <span class="contact__marker"></span>
      <div class="contact__name">Dalvik Ostrander</div>
      <div class="contact__role">Photography</div>
      <ul class="contact__list">
        <li class="contact__item">
          <svg viewBox="0 0 16 16" fill="#ffffff"><path d="M3 1h3l1.5 4-2 1.3a9 9 0 0 0 4.2 4.2L11 8.5l4 1.5v3a2 2 0 0 1-2 2A12 12 0 0 1 1 3a2 2 0 0 1 2-2z"/></svg>
          +330 2460-5193
        </li>
        <li class="contact__item">
          <svg viewBox="0 0 16 16" fill="none" stroke="#ffffff" stroke-width="1.5"><rect x="1" y="3" width="14" height="10"/><path d="M1 3l7 6 7-6"/></svg>
          info@tavorelstudio.com
        </li>
        <li class="contact__item">
          <svg viewBox="0 0 16 16" fill="none" stroke="#ffffff" stroke-width="1.3"><circle cx="8" cy="8" r="6.5"/><path d="M1.5 8h13M8 1.5c-3 3.5-3 9.5 0 13M8 1.5c3 3.5 3 9.5 0 13"/></svg>
          www.tavorelstudio.com
        </li>
      </ul>
    </div>

    <div class="edge-band"></div>
  </section>
</body>
</html>
```